Company brochure for our unique consulting business

We are a small consulting business offering a unique set of services to our clients.. In simple terms we are a business improvement consultancy helping our clients get the best out of their businesses. We work with clients across multiple sectors and deliver a variety of services. We want to put together a brochure to cover these main themes:1. Who we are2. What we do3. The type of people we employ4. The sectors we work inWhile the brochure needs to have a certain corporate feel to it, we don't want it to be "boring" or "stiff". We would like it to have a slightly "friendly" or "informal" feel to it, to reflect the type of organisation we are.We have a company website http://halvorkeyadvisory.example , however we do not want to directly replicate the content or feel as we recognise it needs updating.We would like the brochure to be A4 portrait format. We anticipate requiring 12 sides (including covers) but we are happy to be guided on this based on the content we have provided.The attached ppt file gives the detail of the content to be included and also shows the proposed pagination. For the front cover we would like to try 2 versions, one with the HKA logo and one with the Halvor Key Advisory logo (a file of both is attached)One of the most important pages will be the "Our Services" page. We would like this to cover the centre fold. In the ppt file we have shown an example layout, but this is where we need most help - we are clearly not graphic designers! This page will be the most used page in sales meetings etc.Also attached is the following:1. file for our HalvorKey Advisory company logo.2. File for our HKA company logo3. Files for Oren's signatures (for under photos) - Duncan's to follow4. Photo of Oren & Duncan (person in purple shirt to be cropped out)Thank you and really excited to see what everyone comes back with.Oren & Duncan

Target Market(s)

Very broad - Manufacturing, Healthcare, Hospitality

Industry/Entity Type

Management Consulting

Font styles to use
Other font styles liked:
• We use Swiss721, but happy to be guided by designer

Colors
3276b5
85abd2
0355a3
333333
5c5c5c
9d9d9d
d9d9d9

Requirements
Must have
• Corporate feel
Nice to have
• Slightly friendly feel
• Our standard "blue" is (CORRECTION) - R55 G96 B146 #376092 and our standard grey is R197 G178, B179 - #B3B2B2, which we would like to keep, but other colours we are happy to be guided on. Brand guidelines attached.

```html
<!DOCTYPE html>
<html lang="en">
<head>
<meta charset="UTF-8">
<title>Our Sectors</title>
<link rel="stylesheet" href="https://fonts.googleapis.com/css2?family=Archivo:wght@700;800&family=Inter:wght@400;500&display=swap">
<style>
  :root {
    --blue-bright: #3b72f0;
    --blue-deep: #0b2a8f;
    --blue-header: #2a5de8;
    --blue-sky: #5f9cf5;
    --rule-dark: #3f4a55;
    --grey-corner: #c4cacc;
    --ink: #1f2328;
    --white: #ffffff;
  }
  * { margin: 0; padding: 0; box-sizing: border-box; }
  html, body { width: 848px; height: 1200px; overflow: hidden; background: var(--white); }
  .page { position: relative; width: 848px; height: 1200px; overflow: hidden; background: var(--white); }

  .page-header {
    position: absolute; left: 0; top: 0; width: 848px; height: 124px;
    background: linear-gradient(90deg, var(--blue-header) 0%, #2f66ec 45%, var(--blue-sky) 100%);
  }
  .page-header__skyline {
    position: absolute; right: 0; top: 0; width: 520px; height: 124px;
    background: linear-gradient(90deg, rgba(40,80,220,0) 0%, rgba(30,70,200,0.55) 50%, rgba(20,60,190,0.75) 100%);
  }
  .page-header__rule {
    position: absolute; left: 0; top: 124px; width: 848px; height: 6px; background: var(--rule-dark);
  }
  .page-title {
    position: absolute; right: 74px; top: 72px;
    font-family: "Archivo", Arial, sans-serif; font-weight: 700; font-size: 31px;
    color: var(--white); text-shadow: 1px 2px 3px rgba(0,0,0,0.45); letter-spacing: 0.2px;
  }

  .sector-list { position: absolute; left: 54px; top: 154px; width: 763px; }
  .sector {
    position: absolute; left: 0; width: 763px; height: 145px; overflow: hidden;
    display: flex; align-items: center;
  }
  .sector--light { background: var(--blue-bright); }
  .sector--dark { background: var(--blue-deep); }
  .sector__name {
    position: relative; z-index: 2; width: 356px; text-align: center;
    font-family: "Archivo", Arial, sans-serif; font-weight: 800; font-size: 29px;
    color: var(--white); letter-spacing: 0.5px;
    text-shadow: 2px 3px 4px rgba(0,0,0,0.55);
  }
  .sector__photo { position: absolute; top: 0; right: 0; width: 430px; height: 145px; }
  .sector--light .sector__photo {
    background: linear-gradient(90deg, var(--blue-bright) 0%, #2d5fd8 35%, #1c3f9e 70%, #5a86e6 100%);
  }
  .sector--dark .sector__photo {
    background: linear-gradient(90deg, var(--blue-deep) 0%, #2447b8 40%, #7e9df0 70%, #3a5fd0 100%);
  }

  .page-footer { position: absolute; left: 0; top: 900px; width: 848px; height: 300px; }
  .page-number {
    position: absolute; left: 789px; top: 1136px;
    font-family: "Inter", Arial, sans-serif; font-size: 19px; font-weight: 400; color: var(--ink);
  }
</style>
</head>
<body>
<div class="page">
  <header class="page-header">
    <div class="page-header__skyline" role="img" aria-label="City skyline of high-rise towers tinted blue"></div>
    <h1 class="page-title">Our Sectors</h1>
  </header>
  <div class="page-header__rule"></div>

  <section class="sector-list">
    <div class="sector sector--light" style="top:0">
      <h2 class="sector__name">FMCG</h2>
      <div class="sector__photo" role="img" aria-label="Supermarket shelves stocked with bottled drinks"></div>
    </div>
    <div class="sector sector--dark" style="top:158px">
      <h2 class="sector__name">ENVIRONMENT</h2>
      <div class="sector__photo" role="img" aria-label="Water being poured into a glass"></div>
    </div>
    <div class="sector sector--light" style="top:317px">
      <h2 class="sector__name">RETAIL</h2>
      <div class="sector__photo" role="img" aria-label="Shirts hanging on a clothes rail"></div>
    </div>
    <div class="sector sector--dark" style="top:475px">
      <h2 class="sector__name">FOOD</h2>
      <div class="sector__photo" role="img" aria-label="Plated meal seen from above with a fork"></div>
    </div>
    <div class="sector sector--light" style="top:637px">
      <h2 class="sector__name">FINANCIAL</h2>
      <div class="sector__photo" role="img" aria-label="Close-up of payment cards"></div>
    </div>
    <div class="sector sector--dark" style="top:797px">
      <h2 class="sector__name">CONSTRUCTION</h2>
      <div class="sector__photo" role="img" aria-label="Tower cranes silhouetted against the sky"></div>
    </div>
  </section>

  <svg class="page-footer" width="848" height="300" viewBox="0 900 848 300" aria-hidden="true">
    <polygon points="848,936 848,1200 716,1200 770,1116" fill="var(--grey-corner)"/>
    <polygon points="0,1124 765,1124 718,1200 0,1200" fill="#2f5fcf"/>
    <polygon points="790,1166 848,1166 848,1182 780,1182" fill="var(--rule-dark)"/>
  </svg>
  <div class="page-number">11</div>
</div>
</body>
</html>
```